project proposal

we set up a reseller program proposal. this proposal needs a cover page and inside diagram required to be re-drawed.

-More interesting cover layout

-Better use of type for section headers and featured quotes

Target Market(s)

business partner

Industry/Entity Type

Quotes

```html
<!DOCTYPE html>
<html lang="en">
<head>
<meta charset="utf-8">
<title>Steady Source – Reseller Program Proposal Cover</title>
<link rel="stylesheet" href="https://fonts.googleapis.com/css2?family=Roboto+Condensed:wght@400;700&family=Nothing+You+Could+Do&display=swap">
<style>
  :root {
    --backdrop: #000000;
    --paper: #ffffff;
    --orange: #f26b2a;
    --orange-deep: #ef5a1f;
    --orange-light: #f8a878;
    --amber: #f7a21b;
    --yellow: #ffd21a;
    --green: #1fa84a;
    --green-mid: #3f9a3a;
    --green-dark: #0f5a2a;
    --photo-light: #e8e6e2;
    --photo-mid: #b9b2aa;
    --photo-dark: #3a3634;
  }
  * { margin: 0; padding: 0; box-sizing: border-box; }
  html, body {
    width: 1200px;
    height: 900px;
    overflow: hidden;
    background: var(--backdrop);
  }
  .cover {
    position: absolute;
    left: 281px;
    top: 0;
    width: 637px;
    height: 900px;
    background: var(--paper);
    overflow: hidden;
    font-family: "Roboto Condensed", Arial, sans-serif;
  }
  .cover-art {
    position: absolute;
    left: 0;
    top: 0;
    width: 637px;
    height: 800px;
  }
  .program-title {
    position: absolute;
    left: 110px;
    top: 588px;
    font-family: "Nothing You Could Do", cursive;
    font-size: 40px;
    color: var(--paper);
    white-space: nowrap;
    transform: rotate(-22deg);
    transform-origin: left bottom;
    letter-spacing: 0.5px;
  }
  .brand {
    position: absolute;
    left: 332px;
    top: 728px;
    display: flex;
    align-items: center;
    gap: 14px;
  }
  .brand-name {
    font-family: "Roboto Condensed", Arial, sans-serif;
    font-weight: 700;
    font-size: 46px;
    line-height: 0.95;
    color: var(--green);
    letter-spacing: -0.5px;
  }
  .brand-mark {
    width: 44px;
    height: 44px;
    background: var(--orange-light);
  }
  .phone-tab {
    position: absolute;
    left: 28px;
    top: 793px;
    width: 256px;
    height: 58px;
    background: var(--orange);
    border-radius: 12px 12px 0 0;
    display: flex;
    align-items: center;
    justify-content: center;
    gap: 10px;
    color: var(--paper);
    font-weight: 700;
    font-size: 29px;
  }
  .phone-tab svg { width: 44px; height: 30px; }
  .footer-bands {
    position: absolute;
    left: 0;
    top: 851px;
    width: 637px;
    height: 49px;
  }
  .band-orange { height: 11px; background: var(--orange-deep); }
  .band-green {
    height: 25px;
    background: linear-gradient(90deg, var(--green-dark), var(--green-mid) 60%, var(--green));
    display: flex;
    align-items: center;
    justify-content: flex-end;
    padding-right: 52px;
  }
  .band-dark { height: 13px; background: var(--green-dark); }
  .website {
    color: var(--paper);
    font-size: 12px;
    font-weight: 700;
    font-family: Arial, Helvetica, sans-serif;
  }
</style>
</head>
<body>
  <main class="cover">
    <svg class="cover-art" viewBox="0 0 637 800" xmlns="http://www.w3.org/2000/svg">
      <defs>
        <linearGradient id="greenBand" x1="0" y1="1" x2="1" y2="0">
          <stop offset="0" stop-color="#0f5a2a"/>
          <stop offset="0.5" stop-color="#3f9a3a"/>
          <stop offset="1" stop-color="#9ccc6a"/>
        </linearGradient>
        <linearGradient id="orangeBand" x1="0" y1="1" x2="1" y2="0">
          <stop offset="0" stop-color="#ffd21a"/>
          <stop offset="0.35" stop-color="#f7a21b"/>
          <stop offset="0.7" stop-color="#f58a4a"/>
          <stop offset="1" stop-color="#f9b48c"/>
        </linearGradient>
        <linearGradient id="photoTone" x1="0" y1="0" x2="1" y2="1">
          <stop offset="0" stop-color="#e8e6e2"/>
          <stop offset="0.45" stop-color="#b9b2aa"/>
          <stop offset="1" stop-color="#3a3634"/>
        </linearGradient>
      </defs>
      <path class="band-outer" d="M0 0 H612 V360 C612 580 420 735 0 772 Z" fill="url(#greenBand)"/>
      <path class="band-edge" d="M612 360 C612 580 420 735 0 772" fill="none" stroke="#ffd21a" stroke-width="2"/>
      <path class="band-inner" d="M0 0 H590 V330 C590 560 400 690 0 720 Z" fill="url(#orangeBand)"/>
      <path class="band-inner-edge" d="M0 720 C400 690 590 560 590 330" fill="none" stroke="#fff3c0" stroke-width="2"/>
      <path class="cover-photo" role="img" aria-label="Photo of smiling business partners in a meeting around a table"
            d="M0 0 H452 V330 C448 520 320 615 0 652 Z" fill="url(#photoTone)"/>
    </svg>

    <p class="program-title">Steady Profit Program</p>

    <div class="brand">
      <span class="brand-name">Steady Source</span>
      <span class="brand-mark"></span>
    </div>

    <div class="phone-tab">
      <svg viewBox="0 0 44 30" aria-hidden="true">
        <path d="M2 11 C2 3 42 3 42 11 L42 14 L33 14 L33 9 C28 7 16 7 11 9 L11 14 L2 14 Z" fill="#ffffff"/>
        <path d="M13 12 H31 L36 28 H8 Z" fill="#ffffff"/>
        <circle cx="22" cy="20" r="4.5" fill="#f26b2a"/>
      </svg>
      <span class="phone-number">03-95550148</span>
    </div>

    <div class="footer-bands">
      <div class="band-orange"></div>
      <div class="band-green"><span class="website">www.steadysource.com.au</span></div>
      <div class="band-dark"></div>
    </div>
  </main>
</body>
</html>
```